Digital Medical Care Start-up: New Web Design Needed

We are a startup in Boston, USA. Our current website has mostly acceptable content but looks outdated and it is ineffective. Viewers - especially possible investors - are turned off. It may also have too much content - especially the table. Current site Https://CareLoomKits.com

Business: we produce apps for surgeons to give their patients. The apps describe the medical procedure they will have, how to prepare, what to do to speed recovery, and how to interpret any symptoms. One app for each medical procedure - there are over 200.

LIKES
https://www.kestrivamed.com/
https://www.fenworthclinix.com/en/
https://zorandi.com/about/
DISLIKES
https://plax-ora.com/
https://www.tundravita.com/
https://www.grelvin-clinic.net/
https://www.quessa.com/

Target Market(s)

Audience: Medical Surgeons (customers) and Investors (we will do our first capital raise afterward the new website) in USA.

Coding

Number of Pages Required

Font styles to use
Other font styles liked:
• Candara

Colors
0455a3
f37122

Requirements
Must have
• OUTPUT:
We want a fully Responsive Version.
We do not use Wordpress. The page layout (or template) should be html + css + images + a little JavaScript.
The first page is the landing page. The second page would be the template on which we put the remaining content.
After delivery, the html would be merged into the existing framework. The site needs to be built on a template so it can be managed by an average quasi-tech person, without the need for a coder.

See exisiting company and product logos. They will remain unchanged, so make sure the website is compatable with the current logos.
Nice to have
• We have attached an idea of ours. This is meant for your stimulation, not necessarily for replication. Our attachment does not have all the content details, but the outline is correct.

```html
<!DOCTYPE html>
<html lang="en">
<head>
<meta charset="utf-8">
<title>CareLoomKits – Procedure eCare</title>
<link href="https://fonts.googleapis.com/css2?family=Poppins:ital,wght@0,300;0,400;0,500;0,600;0,700;1,400&display=swap" rel="stylesheet">
<style>
:root{
  --blue:#0455a3;
  --orange:#f37122;
  --ink:#111;
  --white:#fff;
}
*{margin:0;padding:0;box-sizing:border-box}
html,body{width:1200px;height:2343px;overflow:hidden;background:var(--white)}
body{position:relative;font-family:'Poppins',sans-serif;color:var(--ink)}
.abs{position:absolute}
.nowrap{white-space:nowrap}

.site-header{position:absolute;left:0;top:0;width:1200px;height:56px;background:var(--blue)}
.brand{position:absolute;display:flex;align-items:center;gap:9px;color:var(--white);font-weight:600;font-size:19px;letter-spacing:.3px}
.brand-dot{width:31px;height:31px;border-radius:50%;background:var(--white)}
.site-header .brand{left:226px;top:12px}
.main-nav{position:absolute;left:675px;top:20px;display:flex;font-size:10px;font-weight:500;color:var(--white)}
.main-nav span{padding:0 7px;border-left:1.5px solid var(--white);line-height:11px}
.main-nav span:first-child{border-left:none;padding-left:0;text-decoration:underline;text-decoration-color:var(--orange);text-underline-offset:4px;text-decoration-thickness:2px}

.hero-photo{left:273px;top:77px;width:426px;height:258px;border-radius:8px;background:linear-gradient(135deg,#b89a78,#e9e2d8 55%,#c9b9a4)}
.hero-kicker{left:722px;top:76px;font-size:24px;font-weight:300;color:var(--blue)}
.hero-title{left:722px;top:112px;font-size:32px;font-weight:600;line-height:33px;color:var(--ink)}
.hero-sub{left:722px;top:188px;font-size:16.5px;font-style:italic;color:var(--blue);line-height:24px}
.hero-cta{left:722px;top:271px;width:203px;height:64px;border-radius:9px;background:var(--orange);color:var(--white);font-size:28px;font-weight:600;display:flex;align-items:center;justify-content:center}

.tagline{left:235px;top:380px;font-size:19.5px;font-weight:500;color:var(--orange);line-height:29px;white-space:nowrap}

.feature{position:absolute;top:499px;width:275px;text-align:center}
.feature-icon{width:78px;height:78px;border-radius:50%;background:var(--blue);margin:0 auto;display:flex;align-items:center;justify-content:center}
.feature h3{margin-top:22px;font-size:16px;font-weight:500;color:var(--orange);line-height:24px;height:48px}
.feature p{margin-top:12px;font-size:10.2px;color:var(--blue);text-align:left;line-height:15px;white-space:nowrap}

.section-heading{font-size:19.5px;font-weight:500;color:var(--orange)}
.solutions-heading{left:0;width:1200px;text-align:center;top:746px}

.surgery-photo{left:194px;top:849px;width:295px;height:304px;border-radius:8px;background:linear-gradient(160deg,#3f7f5e,#27a89d 50%,#5fc4bb)}
.benefits{left:515px;top:838px;width:520px}
.benefit{height:66px}
.benefit h4{font-size:15px;font-weight:500;color:var(--orange);line-height:22px}
.benefit p{margin:2px 0 0 8px;font-size:9.9px;font-weight:600;color:var(--blue);line-height:15px;white-space:nowrap}

.testimonials-heading{left:226px;top:1205px;font-size:17.5px}
.testimonial{position:absolute;left:226px;width:748px;height:151px;border-radius:9px;background:var(--blue);color:var(--white)}
.avatar{position:absolute;left:16px;top:27px;width:97px;height:97px;border-radius:50%;background:linear-gradient(160deg,#d8c2b0,#8a6e5c)}
.testimonial .quote{position:absolute;left:144px;top:22px;font-size:10px;line-height:15px;white-space:nowrap}
.testimonial .who{position:absolute;left:144px;font-size:10px;line-height:14px;white-space:nowrap}
.who b{font-weight:600;font-size:11px;display:block;margin-bottom:1px}
.who small{font-size:9px}

.groups-heading{left:0;width:1200px;text-align:center;top:1792px;font-size:18px}
.group-art{position:absolute;top:1878px;width:147px;height:147px;border-radius:10px}
.group-label{position:absolute;top:2070px;width:240px;text-align:center;font-size:17.5px;font-weight:500;color:var(--ink)}
.more-bar{left:495px;top:2144px;width:247px;height:22px;border-radius:2px;background:var(--blue)}

.site-footer{position:absolute;left:0;top:2212px;width:1200px;height:131px;background:var(--blue);color:var(--white)}
.site-footer .brand{left:194px;top:48px;font-size:21px}
.site-footer .brand .brand-dot{width:34px;height:34px}
.footer-address{position:absolute;left:545px;top:44px;font-size:11px;line-height:18px}
.footer-address .row{display:flex;align-items:center;gap:7px}
.footer-contact{position:absolute;left:815px;top:43px;width:175px;text-align:center;font-size:11px}
.social{display:flex;justify-content:center;gap:12px;margin:8px 0 6px}
.social i{width:13px;height:13px;border-radius:50%;background:var(--white);display:block}
.footer-contact .mail{display:flex;align-items:center;justify-content:center;gap:6px;font-size:9.5px;white-space:nowrap}
</style>
</head>
<body>

<header class="site-header">
  <div class="brand"><span class="brand-dot"></span>CARELOOMKITS</div>
  <nav class="main-nav"><span>About Us</span><span>Testimonials</span><span>Medical Advisory</span><span>Contact Us</span></nav>
</header>

<div class="abs hero-photo" role="img" aria-label="Photo of a patient with a leg cast holding a tablet showing the app"></div>
<p class="abs hero-kicker">Digitally delivering</p>
<h1 class="abs hero-title">Procedure<br>eCare</h1>
<p class="abs hero-sub">For 100+ procedures<br>Quickly and economically</p>
<div class="abs hero-cta">Contact Us</div>

<p class="abs tagline">we enable clinicians to increase the number of procedures&nbsp; while improving<br>health outcomes</p>

<div class="feature" style="left:166px">
  <div class="feature-icon"><svg width="34" height="30" viewBox="0 0 34 30"><path d="M17 2C8 2 2 7.5 2 14c0 3.5 1.8 6.6 4.6 8.8L5 28l7-3.3c1.6.5 3.3.7 5 .7 9 0 15-5.5 15-12S26 2 17 2z" fill="#fff"/><circle cx="11" cy="14" r="2.2" fill="#0455a3"/><circle cx="17" cy="14" r="2.2" fill="#0455a3"/><circle cx="23" cy="14" r="2.2" fill="#0455a3"/></svg></div>
  <h3>Periop talks</h3>
  <p>lorem ipsum dolor sit amet, consectetur adipiscing elit.<br>nam gravida magna sit amet odio malesuada, at<br>elementum ex accumsan.</p>
</div>
<div class="feature" style="left:461px">
  <div class="feature-icon"><svg width="28" height="34" viewBox="0 0 28 34"><path d="M2 2h16l8 8v22H2z" fill="#fff"/><path d="M18 2v8h8" fill="#0455a3" opacity=".35"/><path d="M4 21h6l2-5 3 9 2-4h7" stroke="#0455a3" stroke-width="2" fill="none"/></svg></div>
  <h3>Interactive Symptom<br>Triage</h3>
  <p>lorem ipsum dolor sit amet, consectetur adipiscing elit.<br>nam gravida magna sit amet odio malesuada, at<br>elementum ex accumsan.</p>
</div>
<div class="feature" style="left:757px">
  <div class="feature-icon"><svg width="40" height="32" viewBox="0 0 40 32"><path d="M15 2C7.5 2 2 6.5 2 12c0 2.8 1.4 5.3 3.8 7L4 24l6-3c1.6.5 3.2.7 5 .7 7.5 0 13-4.5 13-9.7S22.5 2 15 2z" fill="#fff"/><path d="M30 11.5c4.6 1.2 8 4.6 8 8.6 0 2.4-1.2 4.5-3.2 6L36 30l-5.5-2.6c-1.3.3-2.6.5-4 .5-4.2 0-7.8-1.8-9.6-4.5 7.5-.5 13.3-5.6 13.1-11.9z" fill="#fff"/></svg></div>
  <h3>communications</h3>
  <p>lorem ipsum dolor sit amet, consectetur adipiscing elit.<br>nam gravida magna sit amet odio malesuada, at<br>elementum ex accumsan.</p>
</div>

<h2 class="abs section-heading solutions-heading">we have the best ecare solution for surgeries and treatments</h2>

<div class="abs surgery-photo" role="img" aria-label="Photo of a surgical team operating in teal scrubs"></div>
<div class="abs benefits">
  <div class="benefit"><h4>immediate and measurable benefits</h4><p>lorem ipsum dolor sit amet, consectetur adipiscing elit. sed dignissim arcu nunc, vitae suscipit<br>ante tincidunt vitae. praesent in odio ipsum. donec sit amet tempor tellus, vitae vehicula tortor.</p></div>
  <div class="benefit"><h4>improvement in the entire patient journey</h4><p>lorem ipsum dolor sit amet, consectetur adipiscing elit. sed dignissim arcu nunc, vitae suscipit<br>ante tincidunt vitae. praesent in odio ipsum. donec sit amet tempor tellus, vitae vehicula tortor.</p></div>
  <div class="benefit"><h4>provider specific</h4><p>lorem ipsum dolor sit amet, consectetur adipiscing elit. sed dignissim arcu nunc, vitae suscipit<br>ante tincidunt vitae. praesent in odio ipsum. donec sit amet tempor tellus, vitae vehicula tortor.</p></div>
  <div class="benefit"><h4>accessible from any device</h4><p>lorem ipsum dolor sit amet, consectetur adipiscing elit. sed dignissim arcu nunc, vitae suscipit<br>ante tincidunt vitae. praesent in odio ipsum. donec sit amet tempor tellus, vitae vehicula tortor.</p></div>
  <div class="benefit"><h4>no user manual needed</h4><p>lorem ipsum dolor sit amet, consectetur adipiscing elit. sed dignissim arcu nunc, vitae suscipit<br>ante tincidunt vitae. praesent in odio ipsum. donec sit amet tempor tellus, vitae vehicula tortor.</p></div>
</div>

<h2 class="abs section-heading testimonials-heading">Testimonials</h2>

<article class="testimonial" style="top:1260px">
  <div class="avatar" role="img" aria-label="Portrait photo of the physician"></div>
  <p class="quote">“ lorem ipsum dolor sit amet, consectetur adipiscing elit. sed dignissim arcu nunc, vitae suscipit ante<br>tincidunt vitae. praesent in odio ipsum. donec sit amet tempor tellus, vitae vehicula tortor. ut dapibus<br>risus a bibendum sollicitudin. integer tincidunt dapibus maximus. proin sapien erat, ullamcorper eget<br>sollicitudin id, egestas eget quam.”</p>
  <p class="who" style="top:96px"><b>Lorenzo V. Marchetti, MD</b><small>Associate Professor Of Obstetrics, Gynecology,And Reproductive Biology,<br>Bayfield School of Medicine</small></p>
</article>
<article class="testimonial" style="top:1427px">
  <div class="avatar" role="img" aria-label="Portrait photo of the physician"></div>
  <p class="quote">"This Application Will Ensure That Patients Will Have, At Their Fingertips, All The Information<br>They Need To Dramatically Reduce The Anxiety Of Not Knowing What To Expect With Their<br>Procedure. For The Surgeon Or Proceduralist, It Will Help Streamline The Patient Experience,<br>Reduce Extra Work By Minimizing Confusion Or Uncertainty, And Guarantee An Informed<br>Consent Process."</p>
  <p class="who" style="top:108px"><b>Harold T. Brenning, MD</b><small>Former Chair Of Surgery At Stamford, CT</small></p>
</article>
<article class="testimonial" style="top:1595px">
  <div class="avatar" role="img" aria-label="Portrait photo of the physician"></div>
  <p class="quote">"This Platform Embodies THE NOW And THE FUTURE Of Patient-Centered Medicine, Surgery<br>And Perioperative Care As It Optimizes Patient Education And Compliance, And Physician<br>And Practice Efficiency. It Is An Essential Tool To Guide Patients Through Their Treatment<br>And Recovery."</p>
  <p class="who" style="top:94px"><b>Damon P. Wexley MD</b><small>Associate Professor Of Obstetrics, Gynecology, And Reproductive Biology,<br>Bayfield School of Medicine</small></p>
</article>

<h2 class="abs section-heading groups-heading">Clinical Groups</h2>
<div class="group-art" style="left:229px;background:radial-gradient(circle at 60% 45%,#f07080,#e9545f 45%,#f4f1f1 75%)" role="img" aria-label="Illustration of a stomach"></div>
<div class="group-art" style="left:535px;background:radial-gradient(circle at 50% 40%,#e8202a,#f36a6a 40%,#fff 70%)" role="img" aria-label="Illustration of a red heart with a heartbeat line"></div>
<div class="group-art" style="left:814px;background:radial-gradient(ellipse 30% 50% at 50% 50%,#9a86c8,#c9bde3 60%,#fff 100%)" role="img" aria-label="Illustration of a purple baby footprint"></div>
<p class="group-label" style="left:182px">Bariatric</p>
<p class="group-label" style="left:488px">Cardiac Surgery</p>
<p class="group-label" style="left:767px">Fertility Medicine</p>
<div class="abs more-bar"></div>

<footer class="site-footer">
  <div class="brand"><span class="brand-dot"></span>CARELOOMKITS</div>
  <div class="footer-address">
    <div class="row"><svg width="10" height="13" viewBox="0 0 10 13"><path d="M5 0a5 5 0 0 0-5 5c0 3.5 5 8 5 8s5-4.5 5-8a5 5 0 0 0-5-5zm0 7a2 2 0 1 1 0-4 2 2 0 0 1 0 4z" fill="#fff"/></svg><span>CareLoomKits Inc</span></div>
    <div class="row"><span style="width:10px"></span><span>Boston, USA</span></div>
    <div class="row"><svg width="10" height="10" viewBox="0 0 10 10"><path d="M2 0l2 2.5-1.2 1.3c.6 1.3 1.6 2.3 2.9 2.9L7 5.5 10 7.5 8.6 10C4 9.6.4 6 0 1.4z" fill="#fff"/></svg><span>617-555-0143</span></div>
  </div>
  <div class="footer-contact">
    <div>Contact US</div>
    <div class="social"><i></i><i></i><i></i></div>
    <div class="mail"><svg width="14" height="10" viewBox="0 0 14 10"><rect width="14" height="10" rx="1" fill="#fff"/><path d="M1 1l6 4.5L13 1" stroke="#0455a3" stroke-width="1.3" fill="none"/></svg><span>contactus@careloomkitsinc.com</span></div>
  </div>
</footer>

</body>
</html>
```